New custom software business needs a Wordpress site

We need a Wordpress site for a new company based out of Chicago called 'Brackwell Consulting'. Using a mix of on and off-shore resources we build custom software solutions, mainly focusing on small to medium sized companies. We help our customers "aspire" to do great things.
We have a basic site up here: https://brackwellhq.com/. We worked on the content for it but not the branding. For now, this houses all the pages (except for a Contact Us page we'll be adding soon) for the foreseeable future.
We also have a new logo (attached) that we'd like to base the styling/colors on.
Target Market(s)
Small to medium sized companies that require tech resources
Industry/Entity Type
Software
Nice to have
- Teamwork, tech, professional but not elitist

```html
<!DOCTYPE html>
<html lang="en">
<head>
<meta charset="utf-8">
<title>Brackwell Consulting</title>
<link href="https://fonts.googleapis.com/css2?family=Exo+2:wght@500;600;700&family=Montserrat:wght@400;500;600&display=swap" rel="stylesheet">
<style>
:root{
  --navy:#06082e;
  --navy-deep:#0b1240;
  --brand:#0a55b0;
  --brand-light:#3d7cc4;
  --pale:#dfe8f4;
  --white:#ffffff;
  --ink:#111111;
  --body:#2a2a2a;
}
*{box-sizing:border-box;margin:0;padding:0}
html,body{width:677px;height:1200px;overflow:hidden;background:var(--white)}
body{position:relative;font-family:"Montserrat",sans-serif;color:var(--body)}
.abs{position:absolute}

/* Hero */
.hero{left:0;top:0;width:677px;height:381px;overflow:hidden}
.hero-photo{position:absolute;inset:0;background:
  radial-gradient(ellipse at 75% 70%,#7c9ccc 0%,rgba(124,156,204,0) 55%),
  linear-gradient(160deg,#0b0f3a 0%,#1a2a5e 45%,#3e63a0 80%,#6f93c8 100%)}
.wordmark{left:0;width:677px;top:42px;text-align:center;font-family:"Exo 2",sans-serif;font-weight:600;font-size:11px;letter-spacing:1.5px;color:var(--white)}
.nav{left:0;top:86px;width:677px;height:12px;font-family:"Exo 2",sans-serif;font-weight:600;font-size:6px;color:var(--white);text-transform:uppercase}
.nav a{position:absolute;top:0;line-height:12px;color:inherit;text-decoration:none;white-space:nowrap}
.nav .pill{left:163px;width:54px;height:12px;border-radius:6px;background:var(--white);color:var(--brand);text-align:center}
.hero-title{left:0;width:677px;top:138px;text-align:center;font-family:"Exo 2",sans-serif;font-weight:700;font-size:33px;letter-spacing:.5px;color:var(--white)}
.btn{display:flex;align-items:center;justify-content:center;gap:4px;font-family:"Exo 2",sans-serif;font-weight:600;color:var(--white);text-decoration:none}
.btn svg{width:5px;height:7px}
.hero-btn{left:275px;top:203px;width:127px;height:29px;background:var(--navy);font-size:11px}

/* Services */
.section-title{left:0;width:677px;top:424px;text-align:center;font-family:"Exo 2",sans-serif;font-weight:700;font-size:17px;letter-spacing:.5px;color:var(--brand)}
.service{top:0;width:160px;text-align:center}
.service-icon{position:absolute}
.service h3{position:absolute;left:0;width:160px;top:578px;font-family:"Exo 2",sans-serif;font-weight:600;font-size:11px;color:var(--ink);text-align:center}
.service p{position:absolute;top:602px;font-size:7px;line-height:8.7px;color:var(--body);text-align:center}
.service-btn{top:666px;width:123px;height:24px;background:var(--brand);font-size:10px}

/* About */
.about{left:0;top:762px;width:677px;height:380px;overflow:hidden}
.about-photo{position:absolute;inset:0;background:
  radial-gradient(ellipse at 15% 55%,#5f94d2 0%,rgba(95,148,210,0) 45%),
  linear-gradient(180deg,#3c82cf 0%,#2a6fc0 50%,#1e5fb3 100%)}
.about-copy{left:163px;width:352px;font-size:8px;line-height:9.1px;color:var(--white)}
.rule{left:163px;width:35px;height:1.5px;background:var(--white)}

/* Footer */
.footer{left:0;top:1142px;width:677px;height:58px;background:var(--brand);color:var(--white)}
.social{position:absolute;top:19px;height:20px;display:flex;align-items:center;gap:3px;font-size:6px;font-weight:500}
.social i{display:block;width:20px;height:20px;border:1.5px solid var(--white);border-radius:50%}
.footer-name{position:absolute;left:0;width:677px;top:24px;text-align:center;font-family:"Exo 2",sans-serif;font-weight:600;font-size:8.5px}
.copyright{position:absolute;left:486px;top:23px;font-size:9px}
</style>
</head>
<body>

<header class="abs hero">
  <div class="hero-photo" role="img" aria-label="Team collaborating around a laptop, tinted dark blue"></div>
  <div class="abs wordmark">BRACKWELL CONSULTING</div>
  <nav class="abs nav">
    <a class="pill" href="https://brackwellhq.com/">Services &#9662;</a>
    <a style="left:257px" href="https://brackwellhq.com/">Why Brackwell?</a>
    <a style="left:356px" href="https://brackwellhq.com/">Brackwell Leadership</a>
    <a style="left:472px" href="https://brackwellhq.com/">Contact Us</a>
  </nav>
  <h1 class="abs hero-title">BRACKWELL CONSULTING</h1>
  <a class="abs btn hero-btn" href="https://brackwellhq.com/">LEARN MORE
    <svg viewBox="0 0 5 7"><path d="M1 .8 3.8 3.5 1 6.2" fill="none" stroke="#fff" stroke-width="1.4"/></svg></a>
</header>

<main>
  <h2 class="abs section-title">SERVICES OVERVIEW</h2>

  <section class="abs service" style="left:144px">
    <svg class="service-icon" style="left:54px;top:511px" width="52" height="47" viewBox="0 0 52 47">
      <rect x="2" y="2" width="48" height="43" rx="5" fill="none" stroke="#0a55b0" stroke-width="3"/>
      <line x1="2" y1="15" x2="50" y2="15" stroke="#0a55b0" stroke-width="3"/>
      <rect x="9" y="7" width="4" height="4" fill="#0a55b0"/><rect x="18" y="7" width="4" height="4" fill="#0a55b0"/>
      <path d="M16 24 11 30 16 36M36 24 41 30 36 36M29 23 23 37" fill="none" stroke="#0a55b0" stroke-width="3.5" stroke-linecap="round" stroke-linejoin="round"/>
    </svg>
    <h3>Custom Solution Delivery</h3>
    <p style="left:16px;width:128px">Brackwell offers a range of services focused on helping businesses and organizations deliver software solutions to their customers or users.</p>
  </section>
  <a class="abs btn service-btn" style="left:162px" href="https://brackwellhq.com/">LEARN MORE
    <svg viewBox="0 0 5 7"><path d="M1 .8 3.8 3.5 1 6.2" fill="none" stroke="#fff" stroke-width="1.4"/></svg></a>

  <section class="abs service" style="left:372px">
    <svg class="service-icon" style="left:46px;top:500px" width="70" height="70" viewBox="0 0 70 70" fill="none" stroke="#0a55b0" stroke-width="2">
      <circle cx="15" cy="9" r="7"/><circle cx="55" cy="9" r="7"/>
      <path d="M1 41V28q0-9 9-10h10q9 1 9 10v13M41 41V28q0-9 9-10h10q9 1 9 10v13"/>
      <circle cx="35" cy="27" r="8"/>
      <path d="M15 69V55q0-10 10-11h20q10 1 10 11v14"/>
    </svg>
    <h3>Staff Augmentation</h3>
    <p style="left:10px;width:140px">Let Brackwell help you supplement your existing software development teams with additional resources and expertise. We provided access to experienced</p>
  </section>
  <a class="abs btn service-btn" style="left:392px" href="https://brackwellhq.com/">LEARN MORE
    <svg viewBox="0 0 5 7"><path d="M1 .8 3.8 3.5 1 6.2" fill="none" stroke="#fff" stroke-width="1.4"/></svg></a>

  <section class="abs about">
    <div class="about-photo" role="img" aria-label="Business handshake over a desk, tinted bright blue"></div>
  </section>
  <p class="abs about-copy" style="top:791px">Welcome to Brackwell, a software consulting company specializing in serving small to medium size businesses. We understand the unique challenges and opportunities that these companies face, and we are dedicated to helping them succeed through innovative technology solutions.</p>
  <div class="abs rule" style="top:845px"></div>
  <p class="abs about-copy" style="top:864px">Our team of experienced professionals has a diverse range of skills and expertise, making us well-equipped to handle any project, big or small. We specialize in custom software development, working closely with our clients to understand their specific needs and build solutions that meet their requirements.</p>
  <div class="abs rule" style="top:918px"></div>
  <p class="abs about-copy" style="top:937px">From developing web and mobile applications to implementing cloud-based systems and integrating with existing platforms, we have the tools and knowledge to deliver results that drive success. We also offer a range of other services, including IT consulting, project management, and technical support, to help businesses optimize their operations and achieve their goals.</p>
  <div class="abs rule" style="top:999px"></div>
  <p class="abs about-copy" style="top:1018px">At Brackwell, we are committed to delivering high-quality results and exceptional customer service to our small to medium size business clients. We believe that clear communication and collaboration are key to the success of any project, and we work closely with our clients every step of the way to ensure their needs are met and expectations are exceeded.</p>
  <div class="abs rule" style="top:1074px"></div>
  <p class="abs about-copy" style="top:1091px">If you’re a small to medium size business looking for a reliable and experienced software consulting partner, look no further than Brackwell. Contact us today to learn more about how we can help your business grow and thrive through the power of technology.</p>
</main>

<footer class="abs footer">
  <span class="social" style="left:111px"><i></i>Circlely</span>
  <span class="social" style="left:160px"><i></i>Workmesh</span>
  <div class="footer-name">BRACKWELL CONSULTING</div>
  <div class="copyright">Copyright © 2022</div>
</footer>

</body>
</html>
```